High-End audio shop owner needs a business card

I need a personal Business Card for my Audio shop which exists since 1962. We offer high Quality brands, professional Attention and run our own repair-service-department. I look for a design which will be printed on high Quality paper and shall convey trust to the Client that we are very serious. Language is german.

```html
<!DOCTYPE html>
<html lang="de">
<head>
<meta charset="utf-8">
<title>Hi-Fi Klanghaus – Visitenkarte</title>
<link href="https://fonts.googleapis.com/css2?family=Lato:wght@400;700;900&display=swap" rel="stylesheet">
<style>
  :root {
    --stage: #1c1c1c;
    --card: #141414;
    --card-edge: #262626;
    --accent: #f07a12;
    --text-light: #e6e6e6;
    --text-muted: #bdbdbd;
    --rule: #4a4a4a;
  }
  * { margin: 0; padding: 0; box-sizing: border-box; }
  html, body {
    width: 1200px; height: 900px; overflow: hidden;
    background: var(--stage);
    font-family: "Lato", sans-serif;
  }
  .stage { position: relative; width: 1200px; height: 900px; }
  .card {
    position: absolute; left: 320px;
    width: 560px; height: 320px;
    background: var(--card);
    border: 1px solid var(--card-edge);
    border-radius: 22px;
    box-shadow: 0 18px 40px rgba(0,0,0,.55);
    overflow: hidden;
  }
  .card--front { top: 60px; }
  .card--back  { top: 500px; }

  .brand {
    font-family: "Lato", sans-serif;
    font-weight: 900;
    letter-spacing: 1px;
    white-space: nowrap;
  }
  .card--front .brand {
    position: absolute; left: 0; right: 0; top: 136px;
    text-align: center; font-size: 38px; color: var(--text-light);
  }
  .card--back .brand {
    position: absolute; right: 40px; top: 62px;
    font-size: 30px; color: var(--accent);
  }
  .rule { position: absolute; height: 1px; background: var(--rule); }
  .rule--brand { left: 300px; right: 40px; top: 112px; }
  .rule--name  { left: 250px; right: 40px; top: 196px; }

  .holder { position: absolute; left: 40px; top: 168px; }
  .holder__name {
    font-weight: 900; font-size: 22px; color: var(--accent);
    letter-spacing: .5px; line-height: 1; white-space: nowrap;
  }
  .holder__role { font-size: 15px; color: var(--text-muted); margin-top: 4px; }

  .contacts { position: absolute; left: 40px; top: 226px; list-style: none; }
  .contacts li {
    display: flex; align-items: center; gap: 8px;
    font-size: 15px; color: var(--text-light); line-height: 22px; white-space: nowrap;
  }
  .contacts svg { width: 13px; height: 13px; flex: none; }

  .address {
    position: absolute; right: 40px; top: 210px;
    text-align: right; font-size: 15px; line-height: 21px;
    color: var(--text-light); font-style: normal;
  }
</style>
</head>
<body>
<main class="stage">
  <section class="card card--front" aria-label="Vorderseite">
    <div class="brand">Hi-Fi Klanghaus</div>
  </section>

  <section class="card card--back" aria-label="Rückseite">
    <div class="brand">Hi-Fi Klanghaus</div>
    <div class="rule rule--brand"></div>

    <div class="holder">
      <div class="holder__name">MARKUS BERGER</div>
      <div class="holder__role">Managing Director</div>
    </div>
    <div class="rule rule--name"></div>

    <ul class="contacts">
      <li>
        <svg viewBox="0 0 16 16" aria-hidden="true"><path fill="var(--accent)" d="M3 1.5l3 .5 1 3.5-2 1.2a9 9 0 0 0 4.3 4.3l1.2-2 3.5 1 .5 3c0 1-1 1.5-2 1.5C6.5 14.5 1.5 9.5 1.5 3.5c0-1 .5-2 1.5-2z"/></svg>
        044-987 654 321
      </li>
      <li>
        <svg viewBox="0 0 16 16" aria-hidden="true"><rect x="1" y="3" width="14" height="10" rx="1" fill="var(--accent)"/><path d="M1.5 3.5L8 9l6.5-5.5" stroke="var(--card)" stroke-width="1.4" fill="none"/></svg>
        info@klanghaus.ch
      </li>
      <li>
        <svg viewBox="0 0 16 16" aria-hidden="true"><circle cx="8" cy="8" r="7" fill="var(--accent)"/><path d="M1 8h14M8 1c-3 3.5-3 10.5 0 14M8 1c3 3.5 3 10.5 0 14" stroke="var(--card)" stroke-width="1.1" fill="none"/></svg>
        www.klanghaus-hifi.ch
      </li>
    </ul>

    <address class="address">
      17, Lindenstrasse<br>
      Musterstadt, 80331
    </address>
  </section>
</main>
</body>
</html>
```